Twitter and Possible Facebook design for KestrenLtd

We have recently undated our website at www.kestren.co.uk. we are looking for our Twitter page to look good rather than be boring. If a picture for the profile can be created also, utilising the space.

If you require any images please let me know

After looking at some possible design styles - please look at https://chirpwall.example/dunvale_uk or for something a bit more out there https://chirpwall.example/quillmarsh

```html
<!DOCTYPE html>
<html lang="en">
<head>
<meta charset="utf-8">
<title>KestrenLtd – Header Banner</title>
<link rel="stylesheet" href="https://fonts.googleapis.com/css2?family=Roboto:wght@900&family=Lato:wght@400&display=swap">
<style>
  :root {
    --sky-deep: #0a5cae;
    --sky-mid: #1e8fe0;
    --sky-light: #62c4f3;
    --sky-glow: #d4f1ff;
    --globe-core: #e6f7ff;
    --globe-edge: #2a8fd8;
    --touch-tone: #d9c6f0;
    --touch-edge: #8fb7ee;
    --band-dark: rgba(10, 60, 120, 0.55);
    --band-light: rgba(40, 110, 170, 0.45);
    --brand-blue: #2a9cf0;
    --text-white: #ffffff;
    --text-soft: #eaf4fb;
  }
  html, body {
    margin: 0;
    padding: 0;
    width: 1200px;
    height: 400px;
    overflow: hidden;
    background: #ffffff;
  }
  .banner {
    position: relative;
    width: 1200px;
    height: 400px;
    overflow: hidden;
  }
  .banner__backdrop {
    position: absolute;
    inset: 0;
    background:
      radial-gradient(circle at 38% 54%, rgba(255,255,255,0.55) 0%, rgba(255,255,255,0) 6%),
      radial-gradient(circle at 55% 45%, rgba(212,241,255,0.5) 0%, rgba(212,241,255,0) 22%),
      radial-gradient(ellipse at 50% 70%, rgba(98,196,243,0.55) 0%, rgba(98,196,243,0) 45%),
      linear-gradient(100deg, var(--sky-deep) 0%, var(--sky-mid) 35%, #3aa6ea 60%, var(--sky-light) 85%, #3ea9ec 100%);
  }
  .banner__globe {
    position: absolute;
    left: -150px;
    top: 10px;
    width: 390px;
    height: 390px;
    border-radius: 50%;
    background: radial-gradient(circle at 55% 45%, var(--globe-core) 0%, #9fdcfb 30%, #4fb0ec 65%, var(--globe-edge) 100%);
    opacity: 0.85;
  }
  .banner__interface {
    position: absolute;
    left: 800px;
    top: 0;
    width: 400px;
    height: 400px;
    background:
      radial-gradient(ellipse 60px 170px at 140px 250px, var(--touch-tone) 0%, rgba(217,198,240,0.7) 55%, rgba(217,198,240,0) 100%),
      radial-gradient(ellipse 70px 50px at 70px 80px, rgba(230,246,255,0.6) 0%, rgba(230,246,255,0) 100%),
      radial-gradient(ellipse 220px 220px at 280px 160px, rgba(212,241,255,0.55) 0%, rgba(212,241,255,0) 100%);
  }
  .headline-band {
    position: absolute;
    left: 0;
    top: 34px;
    width: 610px;
    height: 122px;
    background: var(--band-dark);
    border-radius: 0 61px 61px 0;
  }
  .headline {
    position: absolute;
    left: 72px;
    top: 45px;
    margin: 0;
    font-family: "Roboto", "Arial", sans-serif;
    font-weight: 900;
    font-size: 42px;
    line-height: 54px;
    letter-spacing: 0.4px;
    color: var(--text-white);
    text-shadow: 2px 3px 3px rgba(0, 20, 50, 0.7);
    text-transform: uppercase;
  }
  .brand {
    position: absolute;
    left: 868px;
    top: 32px;
    height: 32px;
    display: flex;
    align-items: center;
    gap: 10px;
  }
  .brand__dot {
    width: 30px;
    height: 30px;
    border-radius: 50%;
    background: var(--brand-blue);
  }
  .brand__name {
    font-family: "Lato", "Gill Sans", sans-serif;
    font-weight: 400;
    font-size: 26px;
    line-height: 32px;
    color: var(--brand-blue);
  }
  .contact-band {
    position: absolute;
    left: 0;
    top: 296px;
    width: 1200px;
    height: 104px;
    background: var(--band-light);
  }
  .contact {
    position: absolute;
    left: 440px;
    margin: 0;
    font-family: "Lato", "Gill Sans", sans-serif;
    font-size: 17px;
    line-height: 20px;
    letter-spacing: 0.3px;
    color: var(--text-soft);
    text-transform: uppercase;
    white-space: nowrap;
  }
  .contact--address { top: 317px; }
  .contact--lines { top: 353px; }
  .contact__sep { margin: 0 22px; }
</style>
</head>
<body>
  <div class="banner">
    <div class="banner__backdrop" role="img" aria-label="Bright blue technology backdrop crossed by glowing network light trails"></div>
    <div class="banner__globe" role="img" aria-label="Glowing wireframe globe of the Americas on the left edge"></div>
    <div class="banner__interface" role="img" aria-label="Fingertip touching a glowing digital circuit interface on the right"></div>

    <div class="headline-band"></div>
    <h1 class="headline">I.T. &amp; Telecom Experts<br>At Your Fingertips...</h1>

    <div class="brand">
      <span class="brand__dot"></span>
      <span class="brand__name">KestrenLtd</span>
    </div>

    <div class="contact-band"></div>
    <p class="contact contact--address">14 Harrow Lane East, Millbridge, Westshire, MB4 7QT</p>
    <p class="contact contact--lines">Tel: 0808 555 0143<span class="contact__sep">.</span>Fax: 0845 555 0172<span class="contact__sep">.</span>E-mail: sales@kestren.co.uk</p>
  </div>
</body>
</html>
```